Core Values poster for display in office

We want to create a poster that displays our core values which we can print and place in our office and potentially use on our website.

DataHaven is a Cyber Security consultancy that helps its secure its clients from Cyber Criminals.

Our core values are what we live and breath everyday. They are:
- Customer love
- High performing team
- Do the right thing
- An awesome culture
- Innovative

Here they are again with more detail after each:
- Customer love – exchange in abundance
- High performing team – do whatever it takes, no passengers
- Do the right thing – be accountable, maintain our integrity
- An awesome culture – work hard, play hard, collaborate and celebrate success
- Innovative – solving problems with new ideas

We are in the process of rolling out new branding with a load of comic book style super hero's and villains. Attached are some of those images in PDF format for some business card designs for you to review if you want to incorporate, but I will upload these images to this dropbox folder once my designer sends them to me:
https://www.filecrate.example/sh/qpwlzrtkc42hsum/KKTm7VoP2wQ8yE5nLDRxUa91b?dl=0

I stumbled across another business with the same name as us and saw their values poster, which I liked conceptually.
www.datahaven.example
I've attached the image for reference (note this is not our business or values - just saying I like the concept).

Also attached is our logo in EPS format.

We would like the image editing version of the file once complete so we can edit the file in case we change or tweak our values in the near future.

Target Market(s)

This poster is to be displayed internally and maybe on our website in the hiring section

Industry/Entity Type

Office

Colors
0792cd
ffffff
f68e4e
e667a6
fbee3e

Requirements
Must have
• Must have a vibrant, impactful poster that clearly states our core values in a way so that they are understood.
• Must be print ready in high definition (large A2 size poster).
Nice to have
• Integrate our logo

```html
<!DOCTYPE html>
<html lang="en">
<head>
<meta charset="utf-8">
<title>Our Core Values – DataHaven</title>
<link rel="stylesheet" href="https://fonts.googleapis.com/css2?family=Raleway:wght@400;500;600;700&family=Oswald:wght@600;700&family=Alfa+Slab+One&family=Kaushan+Script&family=Graduate&family=Montserrat:ital,wght@0,700;0,800;0,900;1,800&display=swap">
<style>
  :root {
    --blue: #0792cd;
    --blue-deep: #0a79b0;
    --teal-dark: #0e5872;
    --red: #d7141c;
    --orange: #e8a117;
    --ink: #1d1d1d;
    --paper: #ffffff;
    --stage: #e9e9e9;
    --band-dark: #444444;
    --logo-box: #ececec;
  }
  * { margin: 0; padding: 0; box-sizing: border-box; }
  html, body { width: 1200px; height: 1200px; overflow: hidden; background: var(--stage); }
  .poster {
    position: absolute; left: 215px; top: 5px; width: 770px; height: 1190px;
    background: var(--paper); overflow: hidden;
    font-family: "Raleway", sans-serif; color: var(--ink);
  }
  .poster > * { position: absolute; white-space: nowrap; }
  .band-top { left: 0; top: 0; width: 100%; height: 36px;
    background: radial-gradient(circle at 11px 36px, var(--paper) 7px, transparent 7.5px) 0 0 / 22px 36px repeat-x,
                linear-gradient(var(--band-dark) 0 26px, var(--paper) 26px); }
  .band-bottom { left: 0; bottom: 0; width: 100%; height: 40px;
    background: radial-gradient(circle at 11px 0, var(--paper) 7px, transparent 7.5px) 0 0 / 22px 40px repeat-x,
                linear-gradient(var(--paper) 0 10px, var(--blue-deep) 10px); }
  .rule-h, .rule-v { background: var(--blue-deep); }
  .rule-h { height: 1.5px; }
  .rule-v { width: 1.5px; }

  .our-ribbon { left: 212px; top: 58px; width: 346px; height: 62px; }
  .our-ribbon span { position: absolute; left: 0; right: 0; top: 4px; text-align: center;
    color: #fff; font: 600 36px/44px "Raleway", sans-serif; letter-spacing: 1px; }
  .title { left: 0; width: 100%; top: 118px; text-align: center; color: var(--blue);
    font: 400 96px/1 "Raleway", sans-serif; letter-spacing: 1px; }
  .star-rule { height: 14px; }
  .tagline { left: 0; width: 100%; top: 252px; text-align: center; font: 500 25px/1 "Raleway", sans-serif; }

  .customer { left: 42px; top: 304px; color: var(--blue); font: 700 64px/1 "Oswald", sans-serif; letter-spacing: -0.5px; }
  .love { left: 42px; top: 360px; color: var(--red); font: 700 92px/1 "Oswald", sans-serif; }
  .customer-ribbon { left: 40px; top: 458px; width: 240px; height: 60px; }
  .customer-ribbon span { position: absolute; left: 24px; top: 7px; color: #fff; font: 500 21px/23px "Raleway", sans-serif; }

  .art { border-radius: 4px; }

  .high-performing { left: 428px; top: 312px; color: var(--red); font: 700 60px/1 "Oswald", sans-serif;
    letter-spacing: -0.5px; transform: scaleX(0.68); transform-origin: left top; }
  .team { left: 448px; top: 490px; width: 245px; text-align: center; color: var(--teal-dark); font: 900 76px/1 "Montserrat", sans-serif; }
  .team-line-1 { left: 420px; width: 300px; top: 594px; text-align: center; color: var(--blue); font: 500 18px/1 "Raleway", sans-serif; }
  .team-line-2 { left: 420px; width: 300px; top: 616px; text-align: center; font: 800 16px/1 "Montserrat", sans-serif; }
  .team-line-2 .cross { color: var(--red); margin: 0 8px; }

  .right-thing { left: 95px; top: 665px; width: 400px; height: 170px; }
  .right-thing .r1 { position: absolute; left: 95px; top: 10px; width: 275px; height: 66px; transform: rotate(6deg); background: var(--blue-deep);
    color: #fff; font: 400 36px/66px "Alfa Slab One", serif; text-align: center; }
  .right-thing .r2 { position: absolute; left: 30px; top: 82px; width: 272px; height: 62px; transform: rotate(6deg); background: var(--blue-deep);
    color: #fff; font: 400 32px/62px "Alfa Slab One", serif; text-align: center; }
  .accountable { left: 85px; top: 815px; width: 340px; transform: rotate(6deg); transform-origin: left top; }
  .accountable .l1 { padding-left: 96px; font: 500 22px/1 "Raleway", sans-serif; }
  .accountable .l2 { color: var(--orange); font: 800 21px/1.2 "Montserrat", sans-serif; }

  .awesome { left: 500px; top: 715px; width: 250px; text-align: center; color: var(--orange); font: 400 44px/1.05 "Kaushan Script", cursive; }
  .awesome .big { font-size: 54px; }
  .culture { left: 493px; top: 830px; width: 256px; height: 54px; }
  .culture span { position: absolute; left: 0; right: 0; top: 0; text-align: center; color: #fff; font: 800 38px/54px "Montserrat", sans-serif; }
  .work-hard { left: 493px; width: 256px; top: 894px; text-align: center; color: var(--teal-dark); font: 400 32px/1 "Graduate", serif; }
  .play-hard { left: 493px; width: 256px; top: 962px; text-align: center; color: var(--blue); font: 800 38px/1 "Montserrat", sans-serif; }
  .collaborate { left: 493px; width: 256px; top: 1008px; text-align: center; font: 500 20px/1 "Raleway", sans-serif; }
  .celebrate { left: 493px; width: 256px; top: 1034px; text-align: center; color: var(--red); font: italic 800 20px/1 "Montserrat", sans-serif; }

  .innovative { left: 38px; top: 940px; font: 700 62px/1 "Oswald", sans-serif;
    background: repeating-linear-gradient(90deg, var(--red) 0 3px, #f6c8c8 3px 5px);
    -webkit-background-clip: text; background-clip: text; color: transparent; }
  .solving { left: 38px; top: 1007px; color: var(--blue); font: 800 17px/1 "Montserrat", sans-serif; }
  .with-new { left: 118px; top: 1027px; font: 800 19px/1 "Montserrat", sans-serif; }
  .ideas { left: 128px; top: 1046px; color: var(--red); font: 800 32px/1 "Montserrat", sans-serif; }

  .logo-box { left: 488px; top: 1085px; width: 262px; height: 105px; background: var(--logo-box);
    display: flex; align-items: center; justify-content: center; gap: 10px; }
  .logo-box .dot { width: 26px; height: 26px; border-radius: 50%; background: var(--blue); }
  .logo-box .name { font: 600 32px/1 "Raleway", sans-serif; color: var(--blue-deep); }
</style>
</head>
<body>
<main class="poster">
  <div class="band-top"></div>

  <svg class="our-ribbon" viewBox="0 0 346 62" aria-hidden="true">
    <polygon points="0,30 40,30 40,62 0,62 14,46" fill="var(--blue-deep)"/>
    <polygon points="346,30 306,30 306,62 346,62 332,46" fill="var(--blue-deep)"/>
    <rect x="34" y="0" width="278" height="54" fill="var(--blue)"/>
    <line x1="48" y1="27" x2="110" y2="27" stroke="#0a6a9a" stroke-width="1.5"/>
    <line x1="236" y1="27" x2="298" y2="27" stroke="#0a6a9a" stroke-width="1.5"/>
  </svg>
  <div class="our-ribbon"><span>OUR</span></div>

  <h1 class="title">CORE VALUES</h1>
  <svg class="star-rule" style="left:258px;top:226px;width:254px" viewBox="0 0 254 14" aria-hidden="true">
    <line x1="0" y1="7" x2="74" y2="7" stroke="var(--blue-deep)" stroke-width="1.5"/>
    <line x1="180" y1="7" x2="254" y2="7" stroke="var(--blue-deep)" stroke-width="1.5"/>
    <text x="127" y="13" text-anchor="middle" fill="var(--blue)" font-size="15">★ ★ ★</text>
  </svg>
  <p class="tagline">What we Live and Breath Everyday</p>

  <div class="rule-v" style="left:397px;top:310px;height:335px"></div>
  <div class="rule-h" style="left:32px;top:545px;width:338px"></div>
  <div class="rule-h" style="left:410px;top:660px;width:336px"></div>
  <div class="rule-v" style="left:473px;top:805px;height:310px"></div>
  <div class="rule-h" style="left:32px;top:918px;width:410px"></div>

  <h2 class="customer">CUSTOMER</h2>
  <h2 class="love">LOVE</h2>
  <svg class="customer-ribbon" viewBox="0 0 240 60" aria-hidden="true">
    <polygon points="12,0 240,0 240,60 12,60 0,30" fill="var(--blue-deep)"/>
  </svg>
  <div class="customer-ribbon"><span>EXCHANGE<br>IN ABUNDANCE</span></div>
  <div class="art" role="img" aria-label="Superhero silhouette with cape and heart emblem" style="left:240px;top:370px;width:140px;height:160px;background:linear-gradient(135deg,#1aa0b3,#111 60%)"></div>

  <h2 class="high-performing">HIGH PERFORMING</h2>
  <div class="art" role="img" aria-label="Silhouettes of a superhero team standing together" style="left:450px;top:382px;width:243px;height:100px;background:#141414"></div>
  <h2 class="team">TEAM</h2>
  <svg class="star-rule" style="left:455px;top:574px;width:232px" viewBox="0 0 232 14" aria-hidden="true">
    <line x1="0" y1="7" x2="70" y2="7" stroke="var(--red)" stroke-width="1.5"/>
    <line x1="162" y1="7" x2="232" y2="7" stroke="var(--red)" stroke-width="1.5"/>
    <text x="116" y="13" text-anchor="middle" fill="var(--red)" font-size="14">★ ★ ★</text>
  </svg>
  <p class="team-line-1">DO WHATEVER IT TAKES,</p>
  <p class="team-line-2"><span class="cross">✕</span>NO PASSENGERS<span class="cross">✕</span></p>

  <div class="art" role="img" aria-label="Flying superhero silhouette with golden cape" style="left:30px;top:570px;width:160px;height:190px;background:linear-gradient(160deg,#111 55%,#e8a117)"></div>
  <div class="art" role="img" aria-label="Small sun icon" style="left:290px;top:565px;width:64px;height:64px;border-radius:50%;background:radial-gradient(circle,#f5a000 45%,#fde7b0 46%,transparent 70%)"></div>

  <div class="right-thing">
    <div class="r1">★ DO THE ★</div>
    <div class="r2">RIGHT THING</div>
  </div>
  <div class="accountable">
    <p class="l1">BE ACCOUNTABLE,</p>
    <p class="l2">MAINTAIN OUR INTEGRITY</p>
  </div>

  <svg style="left:595px;top:683px;width:70px;height:28px" viewBox="0 0 70 28" aria-hidden="true">
    <text x="35" y="24" text-anchor="middle" fill="var(--red)" font-size="14">★ <tspan font-size="20">★</tspan> ★</text>
  </svg>
  <h2 class="awesome">An<br><span class="big">Awesome</span></h2>
  <svg class="culture" viewBox="0 0 256 54" aria-hidden="true">
    <polygon points="14,0 242,0 256,27 242,54 14,54 0,27" fill="var(--red)"/>
    <polygon points="18,4 238,4 250,27 238,50 18,50 6,27" fill="none" stroke="#fff" stroke-width="1.5" stroke-dasharray="4 3"/>
  </svg>
  <div class="culture"><span>CULTURE</span></div>
  <p class="work-hard">WORK HARD</p>
  <svg class="star-rule" style="left:500px;top:940px;width:240px" viewBox="0 0 240 14" aria-hidden="true">
    <line x1="0" y1="7" x2="74" y2="7" stroke="var(--red)" stroke-width="1.5"/>
    <line x1="166" y1="7" x2="240" y2="7" stroke="var(--red)" stroke-width="1.5"/>
    <text x="120" y="13" text-anchor="middle" fill="var(--red)" font-size="14">★ ★ ★</text>
  </svg>
  <p class="play-hard">PLAY HARD</p>
  <p class="collaborate">COLLABORATE AND</p>
  <p class="celebrate">CELEBRATE SUCCESS</p>

  <h2 class="innovative">INNOVATIVE</h2>
  <p class="solving">SOLVING PROBLEMS</p>
  <p class="with-new">WITH NEW</p>
  <p class="ideas">IDEAS</p>
  <div class="art" role="img" aria-label="Light bulb icon with rays" style="left:40px;top:1030px;width:78px;height:80px;background:radial-gradient(circle at 50% 45%,#f5a000 30%,transparent 55%)"></div>
  <div class="art" role="img" aria-label="Flying superhero silhouette with red cape" style="left:245px;top:1004px;width:212px;height:106px;background:linear-gradient(200deg,var(--red) 35%,#111 65%)"></div>

  <div class="logo-box">
    <span class="dot"></span>
    <span class="name">DataHaven</span>
  </div>

  <div class="band-bottom" style="width:488px"></div>
  <div class="band-bottom" style="left:750px;width:20px"></div>
</main>
</body>
</html>
```